Dryer Vent Cleaning Postcard Design

We need a postcard design for Flue Wranglers, a company that specializes in dryer vent cleaning, repairs and upgrades. Dryer vents need periodic cleaning to avoid lint clogging, dryer malfunction, long dry times and even a house fire. This card will be sent to residential and businesses prospects to introduce them to our services and the importance of maintaining their dryer vents. Our website is @ fluewrangling.com and provides information about our services, photos of our work and our general color scheme (purple/orange). Final print size will be 5x7 horizontal.

Target Market(s)

homeowners and business owners (spas, salons, grooming, gyms, laundrymats, etc)

Requirements
Must have
• Reduce the risk of fire
shortened dry times
lower energy consumption
18000 dryer fires caused in the US per year
Nice to have
• Does your dryer take too long to dry?

```html
<!DOCTYPE html>
<html lang="en">
<head>
<meta charset="utf-8">
<title>Flue Wranglers – Dryer Vent Cleaning Postcard</title>
<link rel="stylesheet" href="https://fonts.googleapis.com/css2?family=Arimo&family=Barlow:wght@600;700&family=Catamaran:wght@400;600;700&display=swap">
<style>
  :root {
    --purple: #8479b8;
    --orange-light: #f39a5a;
    --coral: #ef6e4e;
    --white: #ffffff;
    --appliance-light: #dcd6d2;
    --appliance-dark: #a9a19d;
    --lint: #3a3a3c;
  }
  html, body {
    margin: 0;
    padding: 0;
    overflow: hidden;
    background: var(--purple);
  }
  .postcard {
    position: relative;
    width: 1200px;
    height: 857px;
    overflow: hidden;
    background: var(--purple);
    color: var(--white);
  }
  .wave {
    position: absolute;
    inset: 0;
    width: 1200px;
    height: 857px;
  }
  .wave .band { fill: var(--orange-light); }
  .wave .field { fill: var(--coral); }

  .brand-mark {
    position: absolute;
    left: 60px;
    top: 150px;
    display: flex;
    align-items: center;
    gap: 14px;
    font-family: "Catamaran", sans-serif;
    font-weight: 700;
    font-size: 40px;
    line-height: 1;
    color: var(--white);
  }
  .brand-mark .dot {
    width: 34px;
    height: 34px;
    border-radius: 50%;
    background: var(--white);
  }

  .headline {
    position: absolute;
    left: 412px;
    top: 70px;
    width: 680px;
    margin: 0;
    font-family: "Catamaran", sans-serif;
    font-weight: 700;
    font-size: 84px;
    line-height: 1;
    letter-spacing: -2px;
    white-space: nowrap;
  }
  .tagline {
    position: absolute;
    left: 430px;
    top: 166px;
    margin: 0;
    font-family: "Catamaran", sans-serif;
    font-weight: 400;
    font-size: 54px;
    line-height: 1;
    white-space: nowrap;
  }
  .benefits {
    position: absolute;
    left: 432px;
    top: 228px;
    margin: 0;
    font-family: "Catamaran", sans-serif;
    font-weight: 600;
    font-size: 20px;
    line-height: 26px;
    white-space: nowrap;
  }

  .question {
    position: absolute;
    left: 325px;
    top: 350px;
    margin: 0;
    font-family: "Barlow", sans-serif;
    font-weight: 700;
    font-size: 40px;
    line-height: 51px;
    letter-spacing: 1px;
  }
  .answer {
    position: absolute;
    left: 479px;
    top: 492px;
    margin: 0;
    font-family: "Arimo", sans-serif;
    font-size: 37px;
    line-height: 46px;
  }

  .help {
    position: absolute;
    left: 16px;
    top: 566px;
    margin: 0;
    font-family: "Barlow", sans-serif;
    font-weight: 700;
    font-size: 39px;
    line-height: 48px;
  }
  .call-to-action {
    position: absolute;
    left: 16px;
    top: 684px;
    margin: 0;
    font-family: "Barlow", sans-serif;
    font-weight: 700;
    font-size: 64px;
    line-height: 78px;
    white-space: nowrap;
  }

  .dryer-art {
    position: absolute;
    left: 730px;
    top: 282px;
    width: 460px;
    height: 545px;
    border-radius: 10px;
    background: linear-gradient(160deg, var(--lint) 0%, var(--appliance-light) 30%, var(--appliance-dark) 100%);
  }
</style>
</head>
<body>
  <main class="postcard">
    <svg class="wave" viewBox="0 0 1200 857" aria-hidden="true">
      <path class="band" d="M0,394 C130,396 230,440 300,520 C360,590 400,640 460,685 C560,740 680,748 800,743 C960,736 1080,690 1200,646 L1200,857 L0,857 Z"/>
      <path class="field" d="M0,418 C120,420 215,462 282,540 C340,608 380,660 445,705 C550,762 675,770 800,765 C960,758 1080,712 1200,668 L1200,857 L0,857 Z"/>
    </svg>

    <div class="brand-mark"><span class="dot"></span>Flue Wranglers</div>

    <h1 class="headline">FLUE WRANGLERS</h1>
    <p class="tagline">Dryer Vent Cleaning &amp; Repair</p>
    <p class="benefits">Reduce the risk of fire · Shorter dry times · Lower energy use<br>18,000 dryer fires start in the US every year</p>

    <p class="question">Does your dryer take<br>too long to dry?</p>
    <p class="answer">YES?<br>You may have<br>a dirty dryer.</p>

    <div class="dryer-art" role="img" aria-label="Illustration of a clothes dryer with a cloud of grey lint bursting from its top"></div>

    <p class="help">FLUE WRANGLERS<br>CAN HELP!</p>
    <p class="call-to-action">GET YOUR<br>VENTS CLEANED TODAY!</p>
  </main>
</body>
</html>
```